Prepare a modern, professional business card for Meridel Vantage Advisory (MVA) Our company is in the banking, compliance and finance industry. We provide kiosks, software integration, and compliance guidelines so that banks can "bank" Marijuana Dispensaries with MonLex, Office of Statute Review and NBRA approval.

Target Market(s)

Banks

Industry/Entity Type

Business

Contact Information for Business Card

Peter L Oakridge
Meridel Vantage Advisory
Vice President
4427 Larkspur Crossing Way
Suite 218
Tamsworth, OR 97481
pete@mvalq.com
555-418-7362

Font styles to use
Sans Serif

Requirements
Nice to have
• I like the clean simple appearance of Quince computers. Perhaps the three LETTERS of MVA can be the LOGO on the Card and the Company name could be incorporated in the contact information. Like colors of white, black and gray

```html
<!DOCTYPE html>
<html lang="en">
<head>
<meta charset="utf-8">
<title>Meridel Vantage Advisory – Business Card</title>
<link href="https://fonts.googleapis.com/css2?family=Arimo:wght@400;700&family=PT+Serif:wght@700&display=swap" rel="stylesheet">
<style>
  :root {
    --canvas: #ffffff;
    --card: #ffffff;
    --card-border: #9a9a9a;
    --block-dark: #808080;
    --band-light: #e6e6e6;
    --band-pattern: #ececec;
    --mark: #666666;
    --ink: #2b2b2b;
    --ink-soft: #6e6e6e;
    --label: #4a4a4a;
    --rule: #b4b4b4;
    --icon: #9a9a9a;
  }
  * { margin: 0; padding: 0; box-sizing: border-box; }
  html, body { width: 1200px; height: 976px; overflow: hidden; background: var(--canvas); }
  .canvas { position: relative; width: 1200px; height: 976px; border: 1px solid #d8d8d8; }

  .card {
    position: absolute; left: 334px; width: 531px; height: 311px;
    background: var(--card); border: 1px solid var(--card-border);
    font-family: "Arimo", Arial, sans-serif;
  }
  .card--pattern { top: 133px; }
  .card--plain { top: 531px; }

  .band { position: absolute; left: -1px; right: -1px; top: 34px; height: 54px; }
  .band__fill { position: absolute; left: 34px; right: 34px; top: 0; bottom: 0; }
  .card--pattern .band__fill { background: linear-gradient(90deg, var(--band-pattern), #f3f3f3 30%, var(--band-pattern) 60%, #f0f0f0); }
  .card--plain .band__fill { background: var(--band-light); }
  .band__block { position: absolute; top: 0; width: 35px; height: 54px; background: var(--block-dark); }
  .band__block--left { left: 0; }
  .band__block--right { right: 0; }

  .brand-mark {
    position: absolute; top: -4px;
    font-family: "Arimo", Arial, sans-serif; font-weight: 700;
    font-size: 46px; line-height: 58px; letter-spacing: 0.5px; color: var(--mark);
  }
  .card--pattern .brand-mark { left: 92px; }
  .card--plain .brand-mark { left: 218px; }

  .company-name {
    position: absolute; top: 99px; white-space: nowrap;
    font-family: "PT Serif", Georgia, serif; font-weight: 700;
    font-size: 12.5px; letter-spacing: 0.9px; color: var(--label);
  }
  .card--pattern .company-name { left: 33px; }
  .card--plain .company-name { left: 158px; }

  .person-name {
    position: absolute; right: 33px; top: 168px;
    font-size: 24px; color: var(--ink); white-space: nowrap;
  }
  .divider { position: absolute; left: 34px; top: 205px; width: 332px; height: 4px; }
  .person-title {
    position: absolute; right: 33px; top: 199px;
    font-size: 14px; letter-spacing: 0.2px; color: var(--ink-soft);
  }
  .address {
    position: absolute; right: 33px; top: 224px; text-align: right; white-space: nowrap;
    font-size: 16px; line-height: 19px; color: var(--ink);
  }
  .address__bullet { color: var(--ink-soft); font-size: 12px; margin-right: 8px; vertical-align: 2px; }
  .contacts {
    position: absolute; right: 33px; top: 268px;
    display: flex; align-items: center; gap: 8px;
    font-size: 16px; color: var(--ink); white-space: nowrap;
  }
  .contacts__item { display: flex; align-items: center; gap: 8px; }
  .contacts__icon { width: 19px; height: 19px; display: block; }
</style>
</head>
<body>
<div class="canvas">

  <section class="card card--pattern">
    <div class="band">
      <div class="band__fill" role="img" aria-label="Faint repeating decorative pattern in light gray"></div>
      <div class="band__block band__block--left"></div>
      <div class="band__block band__block--right"></div>
      <div class="brand-mark">MVA</div>
    </div>
    <div class="company-name">MERIDEL VANTAGE ADVISORY</div>
    <div class="person-name">Peter L. Oakridge</div>
    <svg class="divider" viewBox="0 0 332 4" aria-hidden="true">
      <circle cx="2" cy="2" r="2" fill="#9a9a9a"/>
      <line x1="2" y1="2" x2="331" y2="2" stroke="#b4b4b4" stroke-width="1"/>
      <line x1="331" y1="0" x2="331" y2="4" stroke="#b4b4b4" stroke-width="1"/>
    </svg>
    <div class="person-title">VICE PRESIDENT</div>
    <div class="address">
      <div><span class="address__bullet">•</span>4427 Larkspur Crossing Way</div>
      <div>Suite 218 Tamsworth, OR 97481</div>
    </div>
    <div class="contacts">
      <span class="contacts__item">
        <svg class="contacts__icon" viewBox="0 0 19 19" aria-hidden="true"><circle cx="9.5" cy="9.5" r="9.5" fill="#9a9a9a"/><text x="9.5" y="13.5" text-anchor="middle" font-family="Arimo, Arial, sans-serif" font-size="12" fill="#fff">@</text></svg>
        pete@mvalq.com
      </span>
      <span class="contacts__item">
        <svg class="contacts__icon" viewBox="0 0 19 19" aria-hidden="true"><circle cx="9.5" cy="9.5" r="9.5" fill="#9a9a9a"/><circle cx="9.5" cy="9.5" r="6.5" fill="none" stroke="#fff" stroke-width="1.2"/><path d="M7 6.2c.5-.4 1-.3 1.2.2l.5 1.1c.2.4 0 .7-.3 1-.2.2-.2.5 0 .8.4.7.9 1.2 1.5 1.5.3.2.6.1.8-.1.3-.3.6-.4 1-.2l1 .6c.5.3.5.8.1 1.2-.8.8-1.9.8-3 .1-1.2-.7-2.2-1.8-2.8-3-.5-1-.6-2.3 0-3.2z" fill="#fff"/></svg>
        555-418-7362
      </span>
    </div>
  </section>

  <section class="card card--plain">
    <div class="band">
      <div class="band__fill"></div>
      <div class="band__block band__block--left"></div>
      <div class="band__block band__block--right"></div>
      <div class="brand-mark">MVA</div>
    </div>
    <div class="company-name">MERIDEL VANTAGE ADVISORY</div>
    <div class="person-name">Peter L. Oakridge</div>
    <svg class="divider" viewBox="0 0 332 4" aria-hidden="true">
      <line x1="0" y1="2" x2="331" y2="2" stroke="#b4b4b4" stroke-width="1"/>
      <line x1="331" y1="0" x2="331" y2="4" stroke="#b4b4b4" stroke-width="1"/>
    </svg>
    <div class="person-title">VICE PRESIDENT</div>
    <div class="address">
      <div><span class="address__bullet">•</span>4427 Larkspur Crossing Way</div>
      <div>Suite 218 Tamsworth, OR 97481</div>
    </div>
    <div class="contacts">
      <span class="contacts__item">
        <svg class="contacts__icon" viewBox="0 0 19 19" aria-hidden="true"><circle cx="9.5" cy="9.5" r="9.5" fill="#9a9a9a"/><text x="9.5" y="13.5" text-anchor="middle" font-family="Arimo, Arial, sans-serif" font-size="12" fill="#fff">@</text></svg>
        pete@mvalq.com
      </span>
      <span class="contacts__item">
        <svg class="contacts__icon" viewBox="0 0 19 19" aria-hidden="true"><circle cx="9.5" cy="9.5" r="9.5" fill="#9a9a9a"/><circle cx="9.5" cy="9.5" r="6.5" fill="none" stroke="#fff" stroke-width="1.2"/><path d="M7 6.2c.5-.4 1-.3 1.2.2l.5 1.1c.2.4 0 .7-.3 1-.2.2-.2.5 0 .8.4.7.9 1.2 1.5 1.5.3.2.6.1.8-.1.3-.3.6-.4 1-.2l1 .6c.5.3.5.8.1 1.2-.8.8-1.9.8-3 .1-1.2-.7-2.2-1.8-2.8-3-.5-1-.6-2.3 0-3.2z" fill="#fff"/></svg>
        555-418-7362
      </span>
    </div>
  </section>

</div>
</body>
</html>
```